Plancrest needs an updated and catchy flyer/brochure

We need two tasks done. First one is to take our current Sales Brochure and keep the main points as shown but make it more engaging. We like minimalist design and graphical. We are an architectural design and drafting company. Our website is www.plancrest-example.com.au.

The second task is to take our hand drawn sketch and make it a proper A4 flyer. The style should be similar to what the brochure from Task 1 looks like so it all blends in.

**Plancrest is looking for a long term graphic artist to do a large amount of marketing material for the company and the winner of this competition will be given continuous work over the coming years.

```html
<!DOCTYPE html>
<html lang="en">
<head>
<meta charset="UTF-8">
<title>Plancrest – Client Testimonials</title>
<link href="https://fonts.googleapis.com/css2?family=Lato:wght@400;700;900&family=Open+Sans:ital,wght@1,300;1,400&display=swap" rel="stylesheet">
<style>
  :root {
    --brand-blue: #1f5cc0;
    --blue-light: #3b7ad6;
    --blue-dark: #0b3a92;
    --heading-blue: #2458b8;
    --white: #ffffff;
    --ink: #333a44;
    --photo-warm: #8a5a34;
    --photo-dark: #3a2414;
    --photo-stone: #b89a78;
  }
  html, body {
    margin: 0;
    padding: 0;
    overflow: hidden;
    background: #ffffff;
  }
  .flyer {
    position: relative;
    width: 848px;
    height: 1200px;
    overflow: hidden;
    background: var(--white);
    font-family: "Open Sans", Arial, sans-serif;
  }
  .hero-photo {
    position: absolute;
    left: 0;
    top: 0;
    width: 848px;
    height: 413px;
    background:
      linear-gradient(90deg, var(--photo-dark) 0%, var(--photo-warm) 22%, #a0683a 40%, var(--photo-dark) 51%, var(--photo-stone) 58%, #9c7a58 76%, #6b4426 100%);
  }
  .hero-photo::after {
    content: "";
    position: absolute;
    inset: 0;
    background: linear-gradient(180deg, rgba(40,20,8,0.55) 0%, rgba(40,20,8,0) 35%, rgba(40,20,8,0.25) 100%);
  }
  .testimonial-panel {
    position: absolute;
    left: 0;
    top: 413px;
    width: 848px;
    height: 666px;
    background: radial-gradient(ellipse 70% 60% at 50% 50%, var(--blue-light) 0%, var(--brand-blue) 50%, var(--blue-dark) 100%);
  }
  .headline-badge {
    position: absolute;
    left: 306px;
    top: 296px;
    width: 206px;
    height: 206px;
    border-radius: 50%;
    background: var(--white);
    box-shadow: 0 3px 10px rgba(0,0,0,0.35);
    display: flex;
    flex-direction: column;
    align-items: center;
    justify-content: center;
    font-family: "Lato", Arial, sans-serif;
    color: var(--heading-blue);
    text-align: center;
    line-height: 1.05;
  }
  .headline-badge .big { font-size: 42px; font-weight: 900; letter-spacing: 1px; }
  .headline-badge .mid { font-size: 23px; font-weight: 700; }
  .headline-badge .strong { font-size: 25px; font-weight: 900; }
  .testimonials {
    position: absolute;
    left: 57px;
    top: 538px;
    width: 736px;
    margin: 0;
    padding: 0;
    list-style: none;
    color: var(--white);
    font-style: italic;
    font-weight: 300;
    font-size: 13.4px;
    line-height: 19px;
  }
  .testimonials li { margin: 0 0 18px; }
  .site-footer {
    position: absolute;
    left: 0;
    top: 1079px;
    width: 848px;
    height: 121px;
    background: var(--white);
  }
  .brand {
    position: absolute;
    left: 122px;
    top: 30px;
    display: flex;
    align-items: center;
    gap: 14px;
  }
  .brand-mark {
    width: 46px;
    height: 46px;
    background: var(--brand-blue);
  }
  .brand-name {
    font-family: "Lato", Arial, sans-serif;
    font-weight: 900;
    font-size: 44px;
    color: var(--brand-blue);
    letter-spacing: 0.5px;
  }
  .contact {
    position: absolute;
    left: 566px;
    top: 42px;
    margin: 0;
    padding: 0;
    list-style: none;
    font-family: "Lato", Arial, sans-serif;
    color: var(--ink);
  }
  .contact li {
    display: flex;
    align-items: center;
    gap: 10px;
    height: 26px;
  }
  .contact .phone { font-size: 20px; }
  .contact .email { font-size: 15px; }
  .contact svg { width: 18px; height: 18px; fill: var(--ink); }
</style>
</head>
<body>
<div class="flyer">
  <div class="hero-photo" role="img" aria-label="Photograph of a warm timber-beamed living room with a fire bowl beside a stone-walled bathroom with a bathtub"></div>

  <section class="testimonial-panel"></section>

  <div class="headline-badge">
    <span class="big">LOOK</span>
    <span class="mid">WHAT OUR</span>
    <span class="strong">HAPPY CLIENTS</span>
    <span class="mid">ARE SAYING</span>
  </div>

  <ul class="testimonials">
    <li>“We would particularly like to mention that Mara was very diligent and helpful and extremely reliable and attentive to our needs. She came up with some very good options and ideas and we appreciate that very much. We have no hesitation in recommending Plancrest to our colleagues.” Delia Warrick</li>
    <li>“The Plancrest guys completed my project on time and for a great price. I would recommend Plancrest to anyone wanting a good service, cheap rates and good drafting quality. They tick all the boxes.” Glen Hartley, Summit Interiors</li>
    <li>“A big thanks to Tom and the team at Plancrest for doing a superb job on drawings I needed for council approval. The team were professional, easy to deal with and delivered exactly what was needed.” Paul Dravic, Elm Ridge</li>
    <li>“Plancrest has been very professional in the way they have conducted their services. I would recommend Plancrest without hesitation to anyone who is planning a renovation, thanks again.” SamFielding</li>
    <li>“Very good friendly service and great end product” Kai Lorne, Structural Engineer</li>
    <li>“I use Plancrest for all my Structural work and I do this for a reason-they have great rates and produce great drawings!” Grant Ellison, Ellison and Partners</li>
    <li>“Excellent service Tom, great price and fast turnaround time. Thanks”. Ruth Calder - Westvale Estate Manager</li>
    <li>“I am writing to thank you for the excellent service you have provided for me. I found Plancrest on a search engine, after being given a bit of a runaround by an architect. From the moment I stepped into your offices I felt I was in the best possible hands with my house extension drawings and specifications. I have not been let down on one occasion by any of the Plancrest staff. I want to thank you all for your kind, patient and extremely timely responses to all my requests.” Irene Moss</li>
  </ul>

  <footer class="site-footer">
    <div class="brand">
      <div class="brand-mark"></div>
      <span class="brand-name">Plancrest</span>
    </div>
    <ul class="contact">
      <li class="phone">
        <svg viewBox="0 0 24 24" aria-hidden="true"><path d="M3 7c0-2 2-3 4-3h10c2 0 4 1 4 3v2h-5V7H8v2H3V7zm3 4h12l2 8c0 1-1 1-1 1H5s-1 0-1-1l2-8zm6 2a3 3 0 100 6 3 3 0 000-6z"/></svg>
        1300 555 018
      </li>
      <li class="email">
        <svg viewBox="0 0 24 24" aria-hidden="true"><path d="M2 5h20v14H2V5zm2 2v.5l8 5 8-5V7H4zm0 2.8V17h16V9.8l-8 5-8-5z"/></svg>
        info@plancrest-example.com.au
      </li>
    </ul>
  </footer>
</div>
</body>
</html>
```